Wedding "Survival Kit" Bag label

I saw a "Wedding Week Survival Kit" that someone create via this site. They had the same design printed twice (facing opposite directions) on the front of the oversized card and then folded it to top off a bag filled with goodies for their guests. That is what I'm looking to go as well as need help with the design for the card. We are getting married in the Riviera Maya on August 2nd, 2015 and both love very modern designs. Our names are Marisol Tepp and Oskar Velminek.

We would like the label to say something like "Wedding Survival Kit" and have some type of cool, abs tract logo that includes our first names, the location and maybe even the date. Feel free to visit our wedding website for inspiration: www.marisolandoskar-example.com

Industry/Entity Type

Wedding

Font styles to use
Other font styles liked:
• Chalkduster or anything fun

Requirements
Must have
• A fun flare to it!! Bright colors are encouraged!
Should not have
• Traditional boring fonts, or basic design

```html
<!DOCTYPE html>
<html lang="en">
<head>
<meta charset="utf-8">
<title>Wedding Survival Kit Bag – Marisol &amp; Oskar</title>
<link rel="stylesheet" href="https://fonts.googleapis.com/css2?family=Cabin+Sketch:wght@400;700&family=Kaushan+Script&family=Fredoka:wght@600&display=swap">
<style>
  :root {
    --kraft-light: #d9c6a8;
    --kraft-mid: #c9b08c;
    --kraft-dark: #b8997a;
    --orange: #f5a623;
    --orange-light: #fbc45a;
    --ribbon-brown: #7a3f24;
    --ribbon-brown-dark: #5a2c17;
    --ink: #2b1a10;
    --green: #a9c93e;
    --green-bright: #9cc42a;
    --green-pale: #dbe9a9;
    --white: #ffffff;
    --badge-face: #f4f4f4;
  }
  * { margin: 0; padding: 0; box-sizing: border-box; }
  html, body { width: 1200px; height: 654px; overflow: hidden; }
  .label {
    position: relative;
    width: 1200px;
    height: 654px;
    overflow: hidden;
  }
  .backdrop {
    position: absolute;
    inset: 0 0 98px 0;
    background: radial-gradient(ellipse at 55% 45%, var(--kraft-light) 0%, var(--kraft-mid) 65%, var(--kraft-dark) 100%);
  }
  .emblem {
    position: absolute;
    left: 0;
    top: 0;
    width: 420px;
    height: 560px;
  }
  .ribbon-name {
    font-family: "Kaushan Script", cursive;
    font-size: 33px;
    fill: var(--ink);
  }
  .ribbon-amp { font-size: 36px; }
  .monogram-name {
    font-family: "Cabin Sketch", cursive;
    font-weight: 700;
    font-size: 32px;
    fill: var(--ribbon-brown);
  }
  .title {
    position: absolute;
    left: 390px;
    top: 228px;
    font-family: "Cabin Sketch", cursive;
    font-weight: 700;
    line-height: 1;
  }
  .title-lead {
    display: block;
    color: var(--orange);
    font-size: 80px;
    margin-left: 14px;
    letter-spacing: 1px;
  }
  .title-main {
    display: block;
    color: var(--green-bright);
    font-size: 110px;
    margin-top: -8px;
    letter-spacing: 1px;
  }
  .footer-band {
    position: absolute;
    left: 0;
    bottom: 0;
    width: 1200px;
    height: 98px;
    background: var(--green);
  }
  .venue {
    position: absolute;
    left: 30px;
    top: 26px;
    font-family: "Cabin Sketch", cursive;
    font-weight: 700;
    font-size: 42px;
    line-height: 1;
    color: var(--green-pale);
  }
  .wedding-date {
    font-family: "Fredoka", sans-serif;
    font-weight: 600;
    color: var(--white);
    text-shadow: 2px 2px 0 rgba(60, 60, 20, 0.55);
    white-space: nowrap;
    line-height: 1;
  }
  .date-day, .date-suffix, .date-rest { position: absolute; }
  .date-day { left: 918px; top: 10px; font-size: 72px; }
  .date-suffix { left: 960px; top: 10px; font-size: 36px; }
  .date-rest { left: 964px; top: 46px; font-size: 30px; }
</style>
</head>
<body>
<main class="label">
  <div class="backdrop" role="img" aria-label="Brown and beige gingham check pattern on crumpled kraft paper"></div>

  <svg class="emblem" viewBox="0 0 420 560" xmlns="http://www.w3.org/2000/svg">
    <circle cx="207" cy="165" r="152" fill="var(--orange)"/>
    <circle cx="207" cy="165" r="140" fill="var(--orange-light)"/>
    <circle cx="207" cy="165" r="118" fill="var(--badge-face)" stroke="var(--ribbon-brown)" stroke-width="4"/>
    <text class="monogram-name" x="207" y="158" text-anchor="middle">Marisol</text>
    <text class="monogram-name" x="207" y="194" text-anchor="middle">&amp; Oskar</text>

    <polygon points="330,300 380,305 362,345 380,392 330,392" fill="var(--ribbon-brown)"/>
    <polygon points="110,470 365,470 332,528 230,505" fill="var(--ribbon-brown-dark)"/>

    <polygon points="80,290 355,282 358,352 84,358" fill="var(--orange)"/>
    <text class="ribbon-name" x="219" y="333" text-anchor="middle">Oskar Velminek</text>

    <polygon points="57,363 393,363 393,423 57,423" fill="var(--orange-light)"/>
    <line x1="100" y1="393" x2="180" y2="393" stroke="var(--ink)" stroke-width="2"/>
    <line x1="270" y1="393" x2="350" y2="393" stroke="var(--ink)" stroke-width="2"/>
    <text class="ribbon-name ribbon-amp" x="225" y="406" text-anchor="middle">&amp;</text>

    <polygon points="93,422 369,418 369,483 95,487" fill="var(--orange)"/>
    <text class="ribbon-name" x="231" y="464" text-anchor="middle">Marisol Tepp</text>
  </svg>

  <h1 class="title">
    <span class="title-lead">Wedding</span>
    <span class="title-main">Survival Kit Bag</span>
  </h1>

  <footer class="footer-band">
    <p class="venue">Riviera Maya</p>
    <p class="wedding-date"><span class="date-day">2</span><span class="date-suffix">nd</span><span class="date-rest">august 2015</span></p>
  </footer>
</main>
</body>
</html>
```